Copper Heron Website

We need a website for our software / project management services company based in South Africa called "Copper Heron". We provide professional services to high value clients in the public and private sectors.

The website must present a highly professional company that exudes quality and confidence.

The theme should be a highly professional subdued look with a fairly limited palette. The neutral tone should be slightly offset with the colours from the company logo. The website should not look dead though, and subtle colour highligting should provide a fresh vibrant feel.

Refer to the current website for general content (www.copperheron.co.za) that may be used. We would also like to make use of social integration and google maps.
Updates

Thanks to all the designers that have participated so far and to those that are cooking something up at this very minute :-)

We have received a lot of designs with elements that we absolutely love. So now the hard work of refining these designs can begin.

We'll try and provide feedback on every design received so far ... and await the beautiful designs that we haven't received yet :-)

Good Luck!

Project Deadline Extended
Reason: After careful consideration we are extending the deadline to make small revisions to some of the designs and to select the top three designs. Thank you for everyone who has made a contribution so far - we have several designs that we like and selecting the best one is proving to be difficult :-)

Target Market(s)

The company deals mostly with other businesses, so mostly B2B.

Industry/Entity Type

Software

Requirements
Nice to have
• Social integration

```html
<!DOCTYPE html>
<html lang="en">
<head>
<meta charset="utf-8">
<title>Copper Heron</title>
<link rel="stylesheet" href="https://fonts.googleapis.com/css2?family=Arimo:ital,wght@0,400;0,700;1,700&family=Encode+Sans+Condensed:wght@600&display=swap">
<style>
  :root {
    --bg: #d3d3d3;
    --page: #ffffff;
    --accent-green: #8dc63f;
    --logo-grey: #6f7073;
    --line: #c9c9c9;
    --nav-text: #111111;
    --nav-active: #d2d2d2;
    --banner-dark: #3b98ba;
    --banner-light: #6cbcd8;
    --muted: #9b9b9b;
    --body-text: #7a7a7a;
    --card-text: #161616;
    --button-dark: #0f7f98;
    --button-light: #3ab5cd;
    --map-tone: #d9dadb;
  }
  * { box-sizing: border-box; margin: 0; padding: 0; }
  html, body { width: 1200px; height: 1200px; overflow: hidden; background: var(--bg); }
  body { font-family: "Arimo", Arial, sans-serif; }

  .stage { width: 1020px; height: 1020px; transform: scale(1.17647); transform-origin: 0 0; position: relative; }
  .top-rule { position: absolute; left: 0; top: 0; width: 1020px; height: 3px; background: var(--accent-green); z-index: 2; }
  .page { position: absolute; left: 30px; top: 0; width: 960px; height: 1020px;
          background: radial-gradient(ellipse 60% 18% at 50% 8%, #fff 60%, #f1f1f1 100%) , var(--page); }

  .brand { position: absolute; left: 300px; top: 86px; display: flex; align-items: center; gap: 16px; }
  .brand-dot { width: 34px; height: 34px; border-radius: 50%; background: var(--accent-green); }
  .brand-name { font-family: "Encode Sans Condensed", "Arial Narrow", sans-serif; font-weight: 600;
                font-size: 62px; color: var(--logo-grey); letter-spacing: -1px; line-height: 1; }

  .main-nav { position: absolute; left: 10px; top: 189px; width: 940px; height: 46px; border: 1px solid var(--line);
              border-radius: 4px; background: linear-gradient(#fff, #f1f1f1); box-shadow: 0 8px 8px -6px rgba(0,0,0,.15); }
  .main-nav ul { list-style: none; display: flex; height: 100%; }
  .main-nav li { font-size: 12px; color: var(--nav-text); display: flex; align-items: center; padding: 0 25px; height: 100%; }
  .main-nav li:first-child { padding: 0 17px 0 25px; border-right: 1px solid #888; height: 36px; margin-top: 4px; }
  .main-nav li.is-active { background: linear-gradient(#ececec, var(--nav-active)); color: #666; padding: 0 15px; margin-left: 5px; }
  .social { position: absolute; right: 12px; top: 6px; display: flex; gap: 10px; }
  .social span { width: 32px; height: 32px; border-radius: 6px; box-shadow: 0 2px 3px rgba(0,0,0,.25); }
  .social .s1 { background: linear-gradient(#4c9ad3, #1f6aa6); }
  .social .s2 { background: linear-gradient(#7fd0de, #3a9fb5); }
  .social .s3 { background: linear-gradient(#5b7fc6, #2f4f98); }

  .intro { position: absolute; left: 10px; top: 252px; width: 940px; height: 482px; border: 1px solid var(--line);
           border-radius: 5px; background: linear-gradient(#f3f3f3, #fff 6%, #fff 88%, #efefef); overflow: hidden; }
  .banner { position: absolute; left: 0; top: 31px; width: 938px; height: 118px;
            background: linear-gradient(90deg, var(--banner-dark), var(--banner-light) 70%, #5aaecd); }
  .banner h1 { position: absolute; left: 24px; top: 17px; color: #fff; font-size: 33px; font-weight: 700; line-height: 39px; letter-spacing: .6px; }
  .banner-photo { position: absolute; left: 700px; top: 0; width: 160px; height: 118px;
                  background: radial-gradient(ellipse at 55% 45%, #bfe6f2, #7fc6dc 50%, rgba(108,188,216,0) 75%); }
  .tagline { position: absolute; left: 24px; top: 167px; font-size: 20px; font-weight: 700; font-style: italic;
             color: var(--muted); line-height: 25px; letter-spacing: .5px; }
  .intro-copy { position: absolute; left: 24px; top: 236px; width: 885px; font-size: 15px; line-height: 19.5px; color: var(--body-text); letter-spacing: .2px; }
  .intro-copy p + p { margin-top: 19px; }

  .card { position: absolute; top: 748px; width: 300px; height: 250px; border: 1px solid var(--line); border-radius: 5px;
          background: linear-gradient(#f2f2f2, #fff 18%, #fff 85%, #efefef); }
  .card-1 { left: 10px; } .card-2 { left: 330px; } .card-3 { left: 650px; }
  .card-title { position: absolute; left: 22px; top: 17px; display: flex; align-items: center; gap: 9px;
                font-size: 21px; font-weight: 700; font-style: italic; color: var(--muted); letter-spacing: .4px; }
  .card-text { position: absolute; left: 22px; top: 62px; width: 258px; font-size: 13px; line-height: 17px; color: var(--card-text); }
  .read-more { position: absolute; right: 16px; bottom: 15px; font-size: 13px; color: var(--card-text); }
  .card-3 .card-title { left: 0; width: 298px; justify-content: center; }
  .map-area { position: absolute; left: 6px; top: 66px; width: 287px; height: 114px; border: 1px solid #bbb;
              background: linear-gradient(135deg, #eaeaea, var(--map-tone) 50%, #c9cbcc); }
  .map-button { position: absolute; left: 44px; top: 186px; width: 214px; height: 36px; border-radius: 6px;
                background: linear-gradient(var(--button-light), var(--button-dark)); box-shadow: 2px 3px 4px rgba(0,0,0,.3);
                color: #fff; font-size: 18px; font-weight: 700; text-align: center; line-height: 36px; letter-spacing: .5px; }
  .map-credit { position: absolute; left: 0; width: 298px; top: 228px; text-align: center; font-size: 11px; color: #444; letter-spacing: 1px; }

  .footer-nav { position: absolute; left: 0; top: 1006px; width: 960px; text-align: center; font-size: 12px; color: #111; word-spacing: 1px; }
  .footer-nav span { margin: 0 6px; }
</style>
</head>
<body>
<div class="stage">
  <div class="top-rule"></div>
  <div class="page">
    <div class="brand">
      <span class="brand-dot"></span>
      <span class="brand-name">Copper Heron</span>
    </div>

    <nav class="main-nav">
      <ul>
        <li>HOME</li>
        <li>COMPANY</li>
        <li class="is-active">PROFESSIONAL SERVICES</li>
        <li>PORTFOLIO</li>
        <li>CONTACT US</li>
      </ul>
      <div class="social" aria-label="Social links">
        <span class="s1"></span><span class="s2"></span><span class="s3"></span>
      </div>
    </nav>

    <section class="intro">
      <div class="banner">
        <h1>Copper Heron is<br>a premium ICT solutions provider</h1>
        <div class="banner-photo" role="img" aria-label="Photo of a hand touching glowing digital screens"></div>
      </div>
      <p class="tagline">which delivers quality software development support services to clients<br>in all sectors of industry.</p>
      <div class="intro-copy">
        <p>Our value proposition builds on customers' needs to successfully implement software development projects within a given set of time, quality and budgetary constraints. Our focus is to provide customers with a full set of products and services to support each phase of the software development lifecycle whilst offering the benefits of flexibility in scaling of resources, cost reduction, improved cost management, access to specialized skills and the ability to focus on strategic business needs.</p>
        <p>Our absolute obsession with delivering quality software artifacts on time and in budget is what differentiates us from our competitors. We are able to live out this passion by partnering with our clients to ensure that the correct people, processes and technology are applied to each software development project.</p>
      </div>
    </section>

    <article class="card card-1">
      <h2 class="card-title"><svg width="36" height="34" viewBox="0 0 36 34"><polygon points="18,1 22.6,12.5 35,13 25.4,20.8 28.8,33 18,26 7.2,33 10.6,20.8 1,13 13.4,12.5" fill="#d0d0d0" stroke="#bdbdbd"/></svg>Lorem ipsum dolor</h2>
      <p class="card-text">Lorem ipsum dolor sit amet, consect-etuer adipiscing elit, sed diam nonummy nibh euismod tincidunt ut laoreet dolore magna aliquam erat volutpat. Ut wisi enim ad minim veniam, quis nostrud exerci tation ullamcorper suscipit lobortis nisl ut aliquip ex ea commodo conse-quat.</p>
      <span class="read-more">read more &gt;&gt;</span>
    </article>

    <article class="card card-2">
      <h2 class="card-title"><svg width="36" height="34" viewBox="0 0 36 34"><polygon points="18,1 22.6,12.5 35,13 25.4,20.8 28.8,33 18,26 7.2,33 10.6,20.8 1,13 13.4,12.5" fill="#d0d0d0" stroke="#bdbdbd"/></svg>Lorem ipsum dolor</h2>
      <p class="card-text">Lorem ipsum dolor sit amet, consect-etuer adipiscing elit, sed diam nonummy nibh euismod tincidunt ut laoreet dolore magna aliquam erat volutpat. Ut wisi enim ad minim veniam, quis nostrud exerci tation ullamcorper suscipit lobortis nisl ut aliquip ex ea commodo conse-quat.</p>
      <span class="read-more">read more &gt;&gt;</span>
    </article>

    <article class="card card-3">
      <h2 class="card-title">Check our location</h2>
      <div class="map-area" role="img" aria-label="Embedded street map showing the office location"></div>
      <div class="map-button">CLICK HERE</div>
      <p class="map-credit">Powered by AtlasMaps</p>
    </article>

    <footer class="footer-nav">Home<span>|</span>Company<span>|</span>Professional services<span>|</span>Portfolio<span>|</span>Contact us</footer>
  </div>
</div>
</body>
</html>
```